KOV Business Card

the business card should be double sided.
Will need to be Korean on one side and english on the other.
it will need to have:

address
website
skype
phone
cell
fax
name
title
email

just put in dummy details to start - i will then give you correct info once we have the format right.

Also - if you feel creative about the logo we are happy to make some amendments to it so it looks right. We are still at early stages with the logo so happy if you have suggestions around the logo concept.
Updates

The deadline for this has been brought forward to Wednesday 11th December. We can not review any designs after this date.

we will need to make a decision by Wednesday 11th December, so please have designs in by this date and not by the deadline set by craftfolio

Target Market(s)

large companies, executives

Industry/Entity Type

Business

Colors

Designer to choose colors to be used in the design.

Requirements
Must have
• double sided - english on one side and korean on the other. we will give you korean wording once we have a design we like.

```html
<!DOCTYPE html>
<html lang="en">
<head>
<meta charset="utf-8">
<title>KOV Business Card</title>
<link rel="stylesheet" href="https://fonts.googleapis.com/css2?family=Open+Sans:wght@400;700&display=swap">
<style>
  :root {
    --backdrop: #9a9a9a;
    --card: #ffffff;
    --ink: #111111;
    --brand-blue: #1a4a9c;
    --icon-blue: #1f56a8;
  }
  * { box-sizing: border-box; margin: 0; padding: 0; }
  html, body {
    width: 1200px; height: 900px; overflow: hidden;
    background: var(--backdrop);
    font-family: "Open Sans", Arial, sans-serif;
  }
  .business-card {
    position: absolute; left: 180px; top: 210px;
    width: 840px; height: 480px;
    background: var(--card);
    box-shadow: 0 6px 18px rgba(0,0,0,0.25);
    overflow: hidden;
    color: var(--ink);
  }
  .brand {
    position: absolute; left: 0; right: 0; top: 110px;
    display: flex; justify-content: center; align-items: center; gap: 14px;
  }
  .brand-mark { width: 26px; height: 26px; background: var(--ink); }
  .brand-name {
    font-weight: 700; font-size: 84px; letter-spacing: 2px; line-height: 1;
    color: var(--ink);
  }
  .band { position: absolute; height: 14px; background: var(--brand-blue); }
  .band-left { left: 0; top: 262px; width: 320px; }
  .band-right { right: 0; top: 304px; width: 300px; }
  .edge-tab {
    position: absolute; right: 0; top: 380px; width: 26px; height: 80px;
    background: var(--brand-blue);
  }
  .holder {
    position: absolute; left: 320px; width: 220px; top: 268px; text-align: center;
  }
  .holder-name { font-weight: 700; font-size: 24px; letter-spacing: 0.5px; line-height: 1.1; }
  .holder-title { font-size: 15px; line-height: 1.3; }
  .contact-row {
    position: absolute; left: 0; right: 0; top: 350px; height: 96px;
    display: flex; font-size: 17px; line-height: 1.5;
  }
  .contact-col { display: flex; flex-direction: column; justify-content: center; }
  .contact-col.phones { padding-left: 70px; width: 255px; }
  .contact-col.online { padding-left: 34px; width: 285px; }
  .contact-col.address { padding-left: 36px; }
  .divider { width: 2px; background: var(--brand-blue); height: 100%; }
  .contact-item { display: flex; align-items: center; gap: 12px; }
  .contact-item svg { width: 18px; height: 18px; flex: none; }
</style>
</head>
<body>
<div class="business-card">
  <div class="brand">
    <span class="brand-mark"></span>
    <span class="brand-name">KOV</span>
  </div>

  <div class="band band-left"></div>
  <div class="band band-right"></div>
  <div class="edge-tab"></div>

  <div class="holder">
    <div class="holder-name">JOHN SMITH</div>
    <div class="holder-title">Director</div>
  </div>

  <div class="contact-row">
    <div class="contact-col phones">
      <div class="contact-item">
        <svg viewBox="0 0 18 18"><circle cx="9" cy="9" r="9" fill="var(--icon-blue)"/><path d="M6 4.5l2 2-1 1.2c.6 1.3 1.7 2.4 3 3l1.2-1 2 2-1.3 1.6C8.4 13 5 9.6 4.7 6z" fill="#fff"/></svg>
        <span>0961 208 437</span>
      </div>
      <div class="contact-item">
        <svg viewBox="0 0 18 18"><circle cx="9" cy="9" r="9" fill="var(--icon-blue)"/><rect x="6" y="4" width="6" height="3" fill="#fff"/><rect x="4" y="7.5" width="10" height="4.5" rx="1" fill="#fff"/><rect x="6" y="11" width="6" height="3" fill="#fff"/></svg>
        <span>0145 732 960</span>
      </div>
      <div class="contact-item">
        <svg viewBox="0 0 18 18"><circle cx="9" cy="9" r="9" fill="var(--icon-blue)"/><rect x="4" y="5.5" width="10" height="7" fill="#fff"/><path d="M4 5.5l5 4 5-4" fill="none" stroke="var(--icon-blue)" stroke-width="1"/></svg>
        <span>0145 732 961</span>
      </div>
    </div>
    <div class="divider"></div>
    <div class="contact-col online">
      <div class="contact-item">
        <svg viewBox="0 0 18 18"><circle cx="9" cy="9" r="9" fill="var(--icon-blue)"/><rect x="6" y="3.5" width="6" height="11" rx="1" fill="#fff"/><rect x="7" y="5" width="4" height="7" fill="var(--icon-blue)"/></svg>
        <span>johnsmith@kov.com.kr</span>
      </div>
      <div class="contact-item">
        <svg viewBox="0 0 18 18"><circle cx="9" cy="9" r="9" fill="var(--icon-blue)"/><path d="M4.5 5.5h9a1 1 0 0 1 1 1v4.5a1 1 0 0 1-1 1H8l-2.5 2v-2h-1a1 1 0 0 1-1-1V6.5a1 1 0 0 1 1-1z" fill="#fff"/><circle cx="6.7" cy="8.8" r=".8" fill="var(--icon-blue)"/><circle cx="9" cy="8.8" r=".8" fill="var(--icon-blue)"/><circle cx="11.3" cy="8.8" r=".8" fill="var(--icon-blue)"/></svg>
        <span>johnsmith</span>
      </div>
      <div class="contact-item">
        <svg viewBox="0 0 18 18"><circle cx="9" cy="9" r="8" fill="none" stroke="var(--icon-blue)" stroke-width="1.6"/><ellipse cx="9" cy="9" rx="3.5" ry="8" fill="none" stroke="var(--icon-blue)" stroke-width="1.2"/><path d="M1 9h16M2.5 5h13M2.5 13h13" stroke="var(--icon-blue)" stroke-width="1.2"/></svg>
        <span>www.kov.com.kr</span>
      </div>
    </div>
    <div class="divider"></div>
    <div class="contact-col address">
      <span>2450 Maplewood Road</span>
      <span>Hillside, Riverton</span>
      <span>Korea</span>
    </div>
  </div>
</div>
</body>
</html>
```